GLP letterhead

We need a letterhead design for our new company based in Los Angeles called "Gold Lantern Pictures". We develop film and television projects. We work with investors, financiers, film production companies, film distribution and sales companies as well as studios. We would like to incorporate our logo (see attached) but make the letterhead simple and elegant. We need to include: logo, company address, phone number and company website.
Updates

Hello designers, Thanks for your submissions. For our letterhead, we are looking for something more simple and elegant. No heavy bars or lines. Make it feel light and clean. Not a lot of ink on the page. Use the logo and contact info but think "clean", "streamlined" and mostly white paper. Looking forward to seeing more... thanks! Gold Lantern Pictures team

Target Market(s)

Studio executives, talent agents and agencies, financiers, investors.

Industry/Entity Type

It Company

Requirements
Must have
• Gold Lantern Pictures logo (see attached). Logo may be cropped and altered appropriately for elegant letterhead design.
• Please include:
• COMPANY ADDRESS:
• Ridgeway Studio Park
• 2850 Halverson Street
• Tower Annex, 6th Floor
• Harbor Point, OR 97412
• COMPANY WEBSITE:
• www.goldlanternpicturesco.example
• COMPANY PHONE NUMBER:
• 541-555-0148

```html
<!DOCTYPE html>
<html lang="en">
<head>
<meta charset="utf-8">
<title>Gold Lantern Pictures — Letterhead</title>
<link href="https://fonts.googleapis.com/css2?family=Source+Sans+3:wght@400;600&display=swap" rel="stylesheet">
<style>
  :root {
    --paper: #ffffff;
    --ink: #231f20;
    --accent: #29a9e1;
    --divider: #9a9a9a;
    --badge: #000000;
  }
  html, body {
    margin: 0;
    padding: 0;
    overflow: hidden;
    background: var(--paper);
  }
  .letterhead {
    position: relative;
    width: 927px;
    height: 1200px;
    background: var(--paper);
    overflow: hidden;
    font-family: "Source Sans 3", "Myriad Pro", Arial, sans-serif;
    color: var(--ink);
  }
  .brand-badge {
    position: absolute;
    left: 389px;
    top: 0;
    width: 167px;
    height: 181px;
    background: var(--badge);
  }
  .brand-mark {
    position: absolute;
    left: 56px;
    top: 42px;
    width: 54px;
    height: 54px;
    border-radius: 50%;
    background: var(--accent);
  }
  .brand-name {
    position: absolute;
    left: 0;
    right: 0;
    top: 112px;
    margin: 0;
    font-size: 14px;
    font-weight: 600;
    letter-spacing: 1.5px;
    line-height: 1.3;
    text-transform: uppercase;
    text-align: center;
    color: var(--accent);
  }
  .contact {
    position: absolute;
    left: 0;
    right: 0;
    top: 1132px;
    text-align: center;
    font-size: 12.5px;
    line-height: 19px;
    font-style: normal;
  }
  .contact p { margin: 0; }
  .contact .label {
    color: var(--accent);
    font-weight: 600;
    margin-right: 4px;
  }
  .contact .sep {
    color: var(--divider);
    margin: 0 12px;
  }
</style>
</head>
<body>
  <main class="letterhead">
    <header class="brand-badge">
      <div class="brand-mark"></div>
      <h1 class="brand-name">Gold Lantern<br>Pictures</h1>
    </header>

    <address class="contact">
      <p class="contact-address">Ridgeway Studio Park 2850 Halverson Street Tower Annex, 6th Floor Harbor Point, OR 97412</p>
      <p class="contact-lines">
        <span class="label">P:</span>541-555-0148<span class="sep">|</span><span class="label">W:</span>www.goldlanternpicturesco.example
      </p>
    </address>
  </main>
</body>
</html>
```